Kestrel Builders Business Card Design Project

Clean sharp business card
Ability to write on back of card
Details for the card -
Address: PO Box 5867, Marlow Creek, Qld, 4215
ABN: 47 305 961 220
BSA LIC 2650874
Ph: 07 3562 4470
Fax: 07 3562 4475
Email: kestrelbuilders@mailbrook.com.au

```html
<!DOCTYPE html>
<html lang="en">
<head>
<meta charset="utf-8">
<title>Kestrel Builders – Business Card</title>
<link rel="stylesheet" href="https://fonts.googleapis.com/css2?family=Merriweather:wght@400;700&display=swap">
<style>
  :root {
    --card-black: #000000;
    --brand-orange: #f07f1e;
    --text-white: #ffffff;
    --name-silver: #c9c9cb;
    --card-w: 1200px;
    --card-h: 726px;
  }
  * { margin: 0; padding: 0; box-sizing: border-box; }
  html, body {
    width: var(--card-w);
    height: var(--card-h);
    overflow: hidden;
    background: var(--card-black);
  }
  .card {
    position: relative;
    width: var(--card-w);
    height: var(--card-h);
    background: var(--card-black);
    font-family: "Merriweather", Georgia, serif;
    color: var(--text-white);
  }
  .brand-name {
    position: absolute;
    top: 200px;
    left: 0;
    width: 100%;
    text-align: center;
    font-weight: 700;
    font-size: 52px;
    letter-spacing: 1px;
    color: var(--name-silver);
  }
  .address-band {
    position: absolute;
    top: 482px;
    left: 0;
    width: 100%;
    height: 62px;
    background: var(--brand-orange);
    display: flex;
    align-items: center;
    justify-content: center;
  }
  .address {
    font-weight: 700;
    font-size: 40px;
    color: var(--text-white);
    line-height: 1;
    white-space: nowrap;
  }
  .details {
    position: absolute;
    left: 0;
    width: 100%;
    text-align: center;
    font-weight: 400;
    font-size: 26px;
    line-height: 1;
    white-space: nowrap;
  }
  .details--registration { top: 584px; }
  .details--contact { top: 630px; }
  .divider {
    color: var(--brand-orange);
    margin: 0 14px;
  }
</style>
</head>
<body>
  <main class="card">
    <div class="brand-name">Kestrel Builders</div>

    <div class="address-band">
      <p class="address">PO Box 5867, Marlow Creek, Qld, 4215</p>
    </div>

    <p class="details details--registration">
      ABN: 47 305 961 220<span class="divider">|</span>BAS LIC 2650874
    </p>
    <p class="details details--contact">
      T. 35624470<span class="divider">|</span>F. 35624475<span class="divider">|</span>E. kestrelbuilders@mailbrook.com.au
    </p>
  </main>
</body>
</html>
```